Design a PowerPoint template for a consultancy organisation

I am after a Powerpoint template including three pages a title slide (that should have a title and subtitle), A title and content slide and a section header slide. I expect the company name and/or logo to be prominent and the colors to work well with the logo colors. I have included a copy of the logo

```html
<!DOCTYPE html>
<html lang="en">
<head>
<meta charset="utf-8">
<title>Parley Works – Presentation Template</title>
<link rel="stylesheet" href="https://fonts.googleapis.com/css2?family=Open+Sans:wght@300;400;600;700&display=swap">
<style>
:root{
  --green:#8cc63f;
  --green-soft:rgba(140,198,63,.88);
  --purple:#6c1fb5;
  --ink:#1d1d1d;
  --grey:#6f6f6f;
  --rule:#9a9a9a;
  --photo-a:#e9e9e9;
  --photo-b:#b9b9b9;
  --white:#ffffff;
}
*{box-sizing:border-box;margin:0;padding:0}
html,body{width:1200px;height:675px;overflow:hidden;background:var(--white);font-family:"Open Sans",Arial,sans-serif;color:var(--ink)}
.stage{position:relative;width:1200px;height:675px;overflow:hidden;background:var(--white)}
.slide{position:absolute;overflow:hidden;background:var(--white);box-shadow:0 2px 8px rgba(0,0,0,.28)}
.abs{position:absolute}
.photo{position:absolute;background:linear-gradient(135deg,var(--photo-a),var(--photo-b))}
.brand{position:absolute;display:flex;flex-direction:column;align-items:center;gap:2px;font-weight:700;color:var(--green);white-space:nowrap;line-height:1}
.brand .mark{background:var(--green);display:block}
.divider{position:absolute;width:1px;background:var(--rule)}
.circle{position:absolute;border-radius:50%;background:var(--green-soft);color:var(--white);display:flex;align-items:center;justify-content:center;font-weight:400;line-height:1}
.heading{position:absolute;font-weight:700;white-space:nowrap;line-height:1.1}
.note{position:absolute;font-size:4.8px;color:var(--grey);line-height:1.35;text-align:center}
.body{position:absolute;font-size:8.4px;line-height:1.28;color:#444}
.pill{position:absolute;border-radius:999px;color:var(--white);display:flex;align-items:center;white-space:nowrap}
.toc-item{position:absolute;width:98px;text-align:center;color:var(--grey)}
.toc-item .num{font-size:23px;line-height:1}
.toc-item .label{font-size:7.5px;margin-top:3px;color:#444}
.toc-item .desc{font-size:5px;margin-top:5px;line-height:1.3}
</style>
</head>
<body>
<main class="stage">

  <!-- Title slide -->
  <section class="slide title-slide" style="left:0;top:0;width:539px;height:300px;box-shadow:none">
    <div class="photo" style="inset:0;background:linear-gradient(160deg,#fafafa 0%,#e4e4e4 55%,#cdcdcd 100%)" role="img" aria-label="Bright meeting room with a long white table"></div>
    <div class="brand" style="left:40px;top:24px;font-size:12px"><span class="mark" style="width:24px;height:24px"></span>Parley Works</div>
    <div class="pill" style="left:112px;top:124px;width:356px;height:54px;background:var(--purple);justify-content:center;font-size:33px;font-weight:400">PRESENTATION TITLE</div>
    <div class="heading" style="left:134px;top:189px;font-size:21px;font-weight:400">PRESENTATION SUBTITLE</div>
  </section>

  <!-- Projects portfolio slide -->
  <section class="slide portfolio-slide" style="left:773px;top:5px;width:418px;height:232px">
    <div class="photo" style="left:0;top:0;width:418px;height:112px;background:linear-gradient(180deg,#d6d6d6,#f4f4f4)" role="img" aria-label="Modern glass office building seen from below"></div>
    <div class="photo" style="left:168px;top:70px;width:86px;height:86px;border-radius:50%;border:5px solid var(--white);background:linear-gradient(135deg,#9a9a9a,#5a5a5a)" role="img" aria-label="Man working on a laptop on a sofa"></div>
    <div class="heading" style="left:72px;top:106px;font-size:16px">PROJECTS</div>
    <div class="heading" style="left:260px;top:106px;font-size:16px">PORTFOLIO</div>
    <div class="abs" style="left:356px;top:108px;width:16px;height:16px;border-radius:50%;background:var(--purple)"></div>
    <p class="body" style="left:66px;top:163px;width:292px;font-size:7.4px;text-align:justify">Venus has a beautiful name and is the second planet from the Sun. It’s terribly hot—even hotter than Mercury—and its atmosphere is extremely poisonous. It’s the second-brightest natural object in the night sky after the Moon</p>
  </section>

  <!-- Title variant slide -->
  <section class="slide title-variant" style="left:539px;top:19px;width:300px;height:153px">
    <div class="photo" style="left:117px;top:0;width:183px;height:153px;background:linear-gradient(90deg,#f2f2f2,#8c8c8c)" role="img" aria-label="Man with a laptop seated in a lounge"></div>
    <div class="circle" style="left:72px;top:14px;width:68px;height:68px"></div>
    <div class="circle" style="left:160px;top:14px;width:68px;height:68px"></div>
    <div class="circle" style="left:266px;top:14px;width:68px;height:68px"></div>
    <div class="brand" style="left:22px;top:14px;font-size:6px"><span class="mark" style="width:12px;height:12px"></span>Parley Works</div>
    <div class="heading" style="left:23px;top:89px;font-size:12.5px">PRESENTATION TITLE</div>
    <div class="heading" style="left:23px;top:106px;font-size:6.5px;font-weight:400">PRESENTATION SUBTITLE</div>
  </section>

  <!-- Section 02 slide -->
  <section class="slide section-two" style="left:322px;top:303px;width:348px;height:129px">
    <div class="photo" style="left:150px;top:0;width:198px;height:129px;background:linear-gradient(90deg,#f0f0f0,#9c9c9c)" role="img" aria-label="Woman talking on the phone"></div>
    <div class="brand" style="left:26px;top:13px;font-size:6px"><span class="mark" style="width:12px;height:12px"></span>Parley Works</div>
    <div class="heading" style="left:86px;top:24px;font-size:12px;color:var(--white)">MARKETING ANALYSIS</div>
    <div class="circle" style="left:80px;top:40px;width:72px;height:72px;font-size:42px">02</div>
    <div class="circle" style="left:184px;top:40px;width:76px;height:76px"></div>
    <p class="note" style="left:82px;top:119px;text-align:left">Here you could describe the topic</p>
  </section>

  <!-- Section 01 slide -->
  <section class="slide section-one" style="left:438px;top:172px;width:323px;height:182px">
    <div class="photo" style="left:100px;top:0;width:223px;height:182px;background:linear-gradient(90deg,#eeeeee,#6e6e6e)" role="img" aria-label="Man working at a desk in a bright office"></div>
    <div class="brand" style="left:22px;top:16px;font-size:6px"><span class="mark" style="width:12px;height:12px"></span>Parley Works</div>
    <div class="divider" style="left:71px;top:13px;height:24px"></div>
    <div class="heading" style="left:81px;top:18px;font-size:13px">ABOUT US</div>
    <div class="circle" style="left:75px;top:35px;width:70px;height:70px;font-size:42px">01</div>
    <div class="circle" style="left:170px;top:35px;width:70px;height:70px"></div>
    <div class="circle" style="left:268px;top:35px;width:70px;height:70px"></div>
    <p class="note" style="left:78px;top:111px;width:64px">Here you could describe the topic of the section</p>
  </section>

  <!-- KPI slide -->
  <section class="slide kpi-slide" style="left:739px;top:211px;width:428px;height:242px">
    <div class="abs" style="left:96px;top:0;width:137px;height:242px;background:var(--purple)"></div>
    <div class="photo" style="left:233px;top:0;width:195px;height:242px;background:linear-gradient(135deg,#d8d8d8,#8a8a8a)" role="img" aria-label="Woman reading a tablet beside an office window"></div>
    <svg class="abs" style="left:0;top:0" width="100" height="242" viewBox="0 0 100 242" aria-hidden="true">
      <g fill="none" stroke="#6c1fb5" stroke-width="2.4">
        <circle cx="53" cy="36" r="16"/><circle cx="53" cy="122" r="16"/><circle cx="53" cy="200" r="16"/>
      </g>
      <g stroke="#9a9a9a" stroke-width=".8">
        <line x1="69" y1="36" x2="100" y2="36"/><line x1="69" y1="122" x2="100" y2="122"/><line x1="69" y1="200" x2="100" y2="200"/>
      </g>
      <g fill="none" stroke="#6c1fb5" stroke-width="1.2">
        <rect x="47" y="30" width="12" height="12" rx="2"/>
        <rect x="47" y="117" width="12" height="9"/><line x1="50" y1="129" x2="56" y2="129"/>
        <rect x="47" y="194" width="12" height="10"/><polyline points="49,201 52,198 54,200 57,196"/>
      </g>
    </svg>
    <div class="heading" style="left:106px;top:22px;font-size:7.5px;font-weight:600;color:var(--white)">NEPTUNE</div>
    <p class="body" style="left:106px;top:35px;width:105px;font-size:8px;color:var(--white)">Neptune is the farthest planet from the Sun</p>
    <div class="heading" style="left:106px;top:99px;font-size:7.5px;font-weight:600;color:var(--white)">MARS</div>
    <p class="body" style="left:106px;top:112px;width:90px;font-size:8px;color:var(--white)">Despite being red, Mars is a cold place, not hot</p>
    <div class="heading" style="left:106px;top:184px;font-size:7.5px;font-weight:600;color:var(--white)">MERCURY</div>
    <p class="body" style="left:106px;top:197px;width:100px;font-size:8px;color:var(--white)">Mercury is the closest planet to the Sun</p>
    <div class="heading" style="left:250px;top:30px;font-size:16px;color:var(--white)">KPI OVERWIEW</div>
  </section>

  <!-- Quote slide -->
  <section class="slide quote-slide" style="left:0;top:322px;width:298px;height:166px">
    <div class="photo" style="inset:0;background:linear-gradient(110deg,#dcdcdc,#f6f6f6 70%)" role="img" aria-label="Long bright office corridor"></div>
    <div class="circle" style="left:-30px;top:-94px;width:190px;height:190px;background:rgba(140,198,63,.7)"></div>
    <div class="brand" style="left:22px;top:12px;font-size:6px;color:var(--white)"><span class="mark" style="width:12px;height:12px;background:var(--white)"></span>Parley Works</div>
    <div class="divider" style="left:67px;top:10px;height:24px;background:var(--white)"></div>
    <div class="heading" style="left:75px;top:15px;font-size:12px;color:var(--white)">ABOUT US</div>
    <p class="abs" style="right:24px;top:58px;text-align:right;font-size:12px;line-height:1.3;white-space:nowrap">“This is a quote. Words full of<br>wisdom that someone important<br>said and can make the reader get<br>inspired.”</p>
    <div class="pill" style="left:208px;top:123px;width:69px;height:12px;background:var(--purple);justify-content:center;font-size:5.3px">—SOMEONE FAMOUS</div>
  </section>

  <!-- Section 03 slide -->
  <section class="slide section-three" style="left:40px;top:480px;width:299px;height:167px">
    <div class="photo" style="left:70px;top:0;width:229px;height:167px;background:linear-gradient(90deg,#f4f4f4,#9a9a9a)" role="img" aria-label="Woman holding a tablet by a window"></div>
    <div class="brand" style="left:22px;top:12px;font-size:5.8px"><span class="mark" style="width:12px;height:12px"></span>Parley Works</div>
    <div class="divider" style="left:68px;top:9px;height:24px"></div>
    <div class="heading" style="left:76px;top:15px;font-size:11.5px">GOALS &amp; STRATEGY</div>
    <div class="circle" style="left:70px;top:31px;width:68px;height:68px;font-size:40px">03</div>
    <div class="circle" style="left:230px;top:31px;width:68px;height:68px"></div>
    <p class="note" style="left:74px;top:105px;width:60px">Here you could describe the topic of the section</p>
  </section>

  <!-- Title and content slide -->
  <section class="slide content-slide" style="left:348px;top:433px;width:418px;height:234px">
    <div class="photo" style="inset:0;background:linear-gradient(180deg,#e6e6e6,#fbfbfb 60%)" role="img" aria-label="Soft architectural background"></div>
    <div class="brand" style="left:32px;top:17px;font-size:8px"><span class="mark" style="width:16px;height:16px"></span>Parley Works</div>
    <div class="divider" style="left:94px;top:14px;height:32px"></div>
    <div class="heading" style="left:104px;top:22px;font-size:17px">ABOUT US</div>
    <p class="body" style="left:39px;top:94px;width:150px">Mercury is the closest planet to the Sun and the smallest one in the Solar System—it’s only a bit larger than our Moon. The planet’s name has nothing to do with the liquid metal since it was named after the Roman messenger god, Mercury</p>
    <div class="divider" style="left:210px;top:92px;height:80px"></div>
    <p class="body" style="left:244px;top:94px;width:145px">Venus has a beautiful name and is the second planet from the Sun. It’s terribly hot—even hotter than Mercury—and its atmosphere is extremely poisonous. It’s the second-brightest natural object in the night sky after the Moon</p>
    <div class="pill" style="left:36px;top:175px;width:98px;height:19px;background:var(--green);font-size:8px;padding-left:10px;gap:18px">
      <svg width="11" height="7" viewBox="0 0 11 7" aria-hidden="true"><ellipse cx="5.5" cy="3.5" rx="5" ry="3" fill="none" stroke="#fff" stroke-width="1"/><circle cx="5.5" cy="3.5" r="1.3" fill="#fff"/></svg>OUR VISION</div>
    <div class="pill" style="left:283px;top:175px;width:98px;height:19px;background:var(--purple);font-size:8px;padding-left:9px;gap:26px">OUR MISSION
      <svg width="10" height="10" viewBox="0 0 10 10" aria-hidden="true"><circle cx="5" cy="5" r="4" fill="none" stroke="#fff" stroke-width="1"/><circle cx="5" cy="5" r="1.5" fill="#fff"/></svg></div>
  </section>

  <!-- Table of contents slide -->
  <section class="slide toc-slide" style="left:778px;top:458px;width:401px;height:198px">
    <div class="brand" style="left:28px;top:4px;font-size:7.5px"><span class="mark" style="width:14px;height:14px"></span>Parley Works</div>
    <div class="divider" style="left:86px;top:2px;height:26px"></div>
    <div class="heading" style="left:97px;top:6px;font-size:15px;color:#7a7a7a">TABLE OF CONTENTS</div>
    <div class="abs" style="left:29px;top:36px;width:98px;height:71px;background:var(--green)"></div>
    <div class="toc-item" style="left:29px;top:44px;color:var(--white)"><div class="num">01</div><div class="label" style="color:var(--white)">ABOUT US</div><div class="desc">Here you could describe the<br>topic of the section</div></div>
    <div class="toc-item" style="left:150px;top:44px"><div class="num">02</div><div class="label">MARKET ANALYSIS</div><div class="desc">Here you could describe the<br>topic of the section</div></div>
    <div class="toc-item" style="left:269px;top:44px"><div class="num">03</div><div class="label">GOALS &amp; STRATEGY</div><div class="desc">Here you could describe the<br>topic of the section</div></div>
    <div class="toc-item" style="left:29px;top:122px"><div class="num">04</div><div class="label">CONTENT PLAN</div><div class="desc">Here you could describe the<br>topic of the section</div></div>
    <div class="toc-item" style="left:150px;top:122px"><div class="num">05</div><div class="label">BUDGET</div><div class="desc">Here you could describe the<br>topic of the section</div></div>
    <div class="toc-item" style="left:269px;top:122px"><div class="num">06</div><div class="label">KPI OVERWIEW</div><div class="desc">Here you could describe the<br>topic of the section</div></div>
  </section>

</main>
</body>
</html>
```